Maple Sprout Menu (Vegetarian Restaurant Concept)

Maple Sprout is a new concept fast casual restaurant
renders are attached so you can see the style of restaurant
Maple Sprowt is a vibrant and modern Vegetarian fast casual restaurant concept that mixes fresh food, energy, great décor, and a comfortable, welcoming atmosphere to provide a memorable and all Vegetarian dining experience.
Our Mission is to be top of mind when consumers think Vegetarian food!
Target Market(s)
the menu is vegetarian and appeals to a broad demographic in USA
Colors
Designer to choose colors to be used in the design.
Requirements
Must have
- well colored and well laid out menu - should not be cartoonish
Nice to have
- For Phots please use the shots in this file:
- https://www.filecrate-example.net/sh/kq7trm2wzl4pnad/BBBxT_qPwLdRNVoE_KMS_Tb?dl=0
- note these are untouched and you are free to change as needed
Should not have
- Should not be cartoonish - nor kives, forks etc in the design

```html
<!DOCTYPE html>
<html lang="en">
<head>
<meta charset="utf-8">
<title>Maple Sprout Menu</title>
<link href="https://fonts.googleapis.com/css2?family=Bebas+Neue&family=Lato:wght@300;400&display=swap" rel="stylesheet">
<style>
  :root{
    --page:#ffffff;
    --wood-light:#c6c6c6;
    --wood-light-2:#bdbdbd;
    --wood-dark:#3d3d3d;
    --wood-dark-2:#4a4a4a;
    --ink:#111111;
    --red:#e8262a;
    --body:#2e2e2e;
    --photo-bg:#f1f1f1;
  }
  *{margin:0;padding:0;box-sizing:border-box}
  html,body{width:1200px;height:1200px;overflow:hidden;background:var(--page)}
  .canvas{position:relative;width:1200px;height:1200px}
  .menu{
    position:absolute;left:5px;top:188px;width:1190px;height:842px;
    background:
      repeating-linear-gradient(90deg, transparent 0 86px, rgba(0,0,0,.05) 86px 88px),
      linear-gradient(180deg,var(--wood-light),var(--wood-light-2));
    overflow:hidden;
  }
  .band{position:absolute;background:
      repeating-linear-gradient(90deg, transparent 0 86px, rgba(0,0,0,.25) 86px 88px),
      linear-gradient(180deg,var(--wood-dark-2),var(--wood-dark));}
  .band--top-left{left:0;top:0;width:312px;height:104px}
  .band--top-right{left:595px;top:0;width:595px;height:104px}
  .band--bottom{left:0;top:811px;width:1190px;height:31px}
  .dots{position:absolute;height:7px;
    background:radial-gradient(circle at 3.5px 3.5px,#fff 3px,transparent 3.5px) 0 0/13px 7px repeat-x;}
  .dots--top-left{left:7px;top:93px;width:305px}
  .dots--top-right{left:592px;top:93px;width:380px}
  .dots--bottom-left{left:7px;top:816px;width:612px}
  .dots--bottom-right{left:888px;top:816px;width:300px}

  .photo{position:absolute;background:var(--photo-bg)}
  .photo--caesar{left:312px;top:0;width:280px;height:178px;
    background:radial-gradient(circle at 50% 52%,#6f8f4a 0 28%,#d9cdb2 29% 37%,var(--photo-bg) 38%)}
  .photo--side-salad{left:306px;top:196px;width:137px;height:120px;
    background:radial-gradient(circle at 50% 50%,#4f6f38 0 33%,#d9cdb2 34% 42%,var(--photo-bg) 43%)}
  .photo--burger{left:455px;top:196px;width:137px;height:120px;
    background:radial-gradient(circle at 50% 50%,#b7874f 0 22%,#d9cdb2 23% 42%,var(--photo-bg) 43%)}
  .photo--toast{left:312px;top:337px;width:274px;height:214px;
    background:radial-gradient(circle at 50% 50%,#7fa043 0 24%,#d9cdb2 25% 40%,var(--photo-bg) 41%)}
  .photo--lettuce-cups{left:0;top:520px;width:292px;height:174px;
    background:radial-gradient(circle at 50% 52%,#8fbf5a 0 30%,#d9cdb2 31% 40%,var(--photo-bg) 41%)}
  .photo--bruschetta{left:619px;top:622px;width:257px;height:220px;
    background:radial-gradient(circle at 50% 50%,#8a1f35 0 22%,#d9cdb2 23% 38%,var(--photo-bg) 39%)}
  .photo--bowl-a{left:899px;top:442px;width:139px;height:122px;
    background:radial-gradient(circle at 50% 50%,#5d7a3e 0 30%,#d9cdb2 31% 40%,var(--photo-bg) 41%)}
  .photo--bowl-b{left:1047px;top:442px;width:133px;height:122px;
    background:radial-gradient(circle at 50% 50%,#c99a55 0 22%,#d9cdb2 23% 40%,var(--photo-bg) 41%)}
  .cloth{position:absolute;left:778px;top:0;width:412px;height:260px}

  .heading{position:absolute;font-family:"Bebas Neue",sans-serif;font-size:50px;line-height:50px;
    color:var(--ink);text-decoration:underline;text-decoration-thickness:4px;text-underline-offset:3px;white-space:nowrap}
  .list{position:absolute;list-style:none}
  .item{position:relative;padding-left:11px}
  .item__name{display:block;font-family:"Bebas Neue",sans-serif;font-size:29px;line-height:30px;color:var(--red);letter-spacing:.2px}
  .item::before{content:"";position:absolute;left:0;top:12px;width:5px;height:5px;border-radius:50%;background:var(--red)}
  .item__desc{display:block;font-family:"Lato",sans-serif;font-weight:300;font-size:14px;line-height:16.5px;color:var(--body);margin:1px 0 6px}
  .item + .item{margin-top:4px}
  .soup-item{position:absolute;left:11px;top:762px;font-family:"Bebas Neue",sans-serif;font-size:29px;line-height:30px;color:var(--red)}
</style>
</head>
<body>
<div class="canvas">
  <section class="menu">
    <div class="band band--top-left"></div>
    <div class="band band--top-right"></div>
    <div class="band band--bottom"></div>
    <div class="dots dots--top-left"></div>
    <div class="dots dots--top-right"></div>
    <div class="dots dots--bottom-left"></div>
    <div class="dots dots--bottom-right"></div>

    <svg class="cloth" viewBox="0 0 412 260" role="img" aria-label="Checked maroon and white table cloth draped over the corner">
      <defs>
        <linearGradient id="clothTone" x1="0" y1="0" x2="1" y2="1">
          <stop offset="0" stop-color="#b9a6a8"/>
          <stop offset="1" stop-color="#6e3a40"/>
        </linearGradient>
      </defs>
      <path d="M0 0 H412 V258 C380 210 360 160 330 150 C300 138 270 110 250 90 C220 70 170 60 140 40 C100 20 50 15 0 0 Z" fill="url(#clothTone)"/>
    </svg>

    <div class="photo photo--caesar" role="img" aria-label="Brussel sprout caesar salad with croutons and dried cranberries in a bowl"></div>
    <div class="photo photo--side-salad" role="img" aria-label="Green salad with avocado and tomatoes in a bowl"></div>
    <div class="photo photo--burger" role="img" aria-label="Veggie burger on slaw in a bowl"></div>
    <div class="photo photo--toast" role="img" aria-label="Avocado toast topped with cherry tomatoes, corn and greens"></div>
    <div class="photo photo--lettuce-cups" role="img" aria-label="Black bean and corn salad in lettuce cups with lime"></div>
    <div class="photo photo--bruschetta" role="img" aria-label="Diced beet bruschetta with basil and balsamic"></div>
    <div class="photo photo--bowl-a" role="img" aria-label="Grain bowl with greens, beets and squash"></div>
    <div class="photo photo--bowl-b" role="img" aria-label="Vegetable melt on toast in a bowl"></div>

    <h2 class="heading" style="left:11px;top:118px">Salads</h2>
    <ul class="list" style="left:11px;top:182px;width:300px">
      <li class="item"><span class="item__name">Brussel Sprout Ceasar</span><span class="item__desc">Little gem romaine, toasted torn bread,<br>parmigiano reggiano</span></li>
      <li class="item"><span class="item__name">Heirloom Beet Salad</span><span class="item__desc">Shaved chioggia beet, roasted golden<br>beet, red quinoa, little gem, arugula,<br>lemon vinaigrette</span></li>
      <li class="item"><span class="item__name">Zesty Black Bean and<br>Corn Salad in Lettuce Cups</span><span class="item__desc">Little gem romaine, toasted torn bread,<br>parmigiano reggiano</span></li>
      <li class="item"><span class="item__name">Green, Red and White</span><span class="item__desc">Spring leaves, cherry tomatoes, avocado,<br>roasted almond and goat cheese</span></li>
    </ul>

    <h2 class="heading" style="left:11px;top:701px">Soup</h2>
    <p class="soup-item">Black Bean Chowder</p>

    <h2 class="heading" style="left:307px;top:566px">Toasts</h2>
    <ul class="list" style="left:306px;top:629px;width:300px">
      <li class="item"><span class="item__name">Everything Avocado Toast</span><span class="item__desc">Avocado on whole grain toast with our<br>signature spice blend</span></li>
      <li class="item"><span class="item__name">Tomato &amp; Beet Bruschetta</span></li>
      <li class="item"><span class="item__name">Vegetable Melt on<br>Garlic Toast</span></li>
    </ul>

    <h2 class="heading" style="left:602px;top:119px;line-height:52px">Burgers, Wraps<br>&amp; Sandwiches</h2>
    <ul class="list" style="left:604px;top:234px;width:285px">
      <li class="item"><span class="item__name">Sweet Potato, Black Bean<br>Veggie Burgers with<br>Cabbage - Pepita Slaw</span></li>
      <li class="item"><span class="item__name">Roasted Vejjie, Arugula<br>and Hummus Wraps</span></li>
      <li class="item"><span class="item__name">Garden Burger</span></li>
      <li class="item"><span class="item__name">Beans and<br>Greens Quesadillas</span><span class="item__desc">Greens, Mexican cheese, beans and<br>avocado, with salsa</span></li>
      <li class="item"><span class="item__name">Vejjie Burrito</span><span class="item__desc">Greens, Mexican cheese, beans, brown<br>rice, roasted chili corn and avocado, with<br>ancho chili salsa, wheat tortilla</span></li>
    </ul>

    <h2 class="heading" style="left:897px;top:118px">Bowls</h2>
    <ul class="list" style="left:899px;top:183px;width:290px">
      <li class="item"><span class="item__name">Roasted Vegetable<br>and Spinach Bowl</span></li>
      <li class="item"><span class="item__name">Sugar Snap Pea and<br>Carrot Soba Noodles</span></li>
      <li class="item"><span class="item__name">Whole Grain and<br>Vegetable Buddha Bowl</span></li>
      <li class="item"><span class="item__name">Orange and Pistacio<br>Quinoa</span></li>
    </ul>

    <h2 class="heading" style="left:897px;top:572px">Dessert</h2>
    <ul class="list" style="left:899px;top:638px;width:290px">
      <li class="item"><span class="item__name">Strawberry Balsamic<br>Ice Cream&nbsp; Sundae</span></li>
      <li class="item"><span class="item__name">Exotic Fruit Bowl</span></li>
      <li class="item"><span class="item__name">White and Dark Oatmeal<br>Cookie</span></li>
    </ul>
  </section>
</div>
</body>
</html>
```